E-commerce Website needs category banner

What we need for our category banner is a clean, predominately black design that showcases the product we are trying to sell (currently only 1), and a few subtle gradients that follow the pattern set by previous designs.

An example will be provided to showcase what we want.

It needs to say:
Outdoor Motion Detection Lighting in large, clear font similar to the example provided.

Please ensure dimensions are as follows: 980x300

Target Market(s)

Senior citizens, businesses, homeowners, families, etc

Industry/Entity Type

Product

Font styles to use
Sans Serif

Requirements
Must have
• It needs to say:
Outdoor Motion Detection Lighting in large, clear font similar to the example provided
980x300 is the required size!
Should not have
• Too much going on- clean and simple please (no crazy fonts, logos, etc)

```html
<!DOCTYPE html>
<html lang="en">
<head>
<meta charset="utf-8">
<title>Outdoor Motion Detection Lighting – Category Banner</title>
<link href="https://fonts.googleapis.com/css2?family=Oswald:wght@600;700&display=swap" rel="stylesheet">
<style>
  :root {
    --bg-deep: #0b0b0b;
    --bg-mid: #262626;
    --bg-glow: #3a3a3a;
    --headline: #ffffff;
    --beam: rgba(255, 255, 255, 0.22);
    --btn-top: #ffa43a;
    --btn-mid: #ff8a12;
    --btn-bottom: #e86a00;
    --btn-text: #1a1a1a;
    --product-light: #f2f2f2;
    --product-shade: #9a9a9a;
  }
  * { margin: 0; padding: 0; box-sizing: border-box; }
  html, body {
    width: 1200px;
    height: 465px;
    overflow: hidden;
    background: var(--bg-deep);
  }
  .banner {
    position: relative;
    width: 1200px;
    height: 465px;
    overflow: hidden;
    background:
      radial-gradient(ellipse 420px 300px at 900px 230px, var(--bg-glow) 0%, rgba(40,40,40,0.6) 45%, rgba(0,0,0,0) 100%),
      linear-gradient(90deg, var(--bg-mid) 0%, #1c1c1c 45%, #141414 75%, var(--bg-deep) 100%);
  }
  .banner__beams {
    position: absolute;
    inset: 0;
  }
  .headline {
    position: absolute;
    left: 68px;
    top: 88px;
    font-family: 'Oswald', sans-serif;
    font-weight: 700;
    color: var(--headline);
    text-transform: uppercase;
    font-size: 80px;
    line-height: 102px;
    letter-spacing: 0.5px;
  }
  .headline__line { display: block; white-space: nowrap; }
  .cta {
    position: absolute;
    left: 67px;
    top: 332px;
    width: 280px;
    height: 61px;
    border-radius: 31px;
    background: linear-gradient(180deg, var(--btn-top) 0%, var(--btn-mid) 50%, var(--btn-bottom) 100%);
    box-shadow: inset 0 2px 0 rgba(255,255,255,0.35);
    display: flex;
    align-items: center;
    padding-left: 76px;
    font-family: 'Oswald', sans-serif;
    font-weight: 700;
    font-size: 27px;
    color: var(--btn-text);
    text-transform: uppercase;
    text-decoration: none;
  }
  .cta__cursor {
    position: absolute;
    left: 222px;
    top: 14px;
  }
  .product-shot {
    position: absolute;
    left: 800px;
    top: 82px;
    width: 245px;
    height: 300px;
    border-radius: 48% 48% 44% 44%;
    background: radial-gradient(ellipse at 40% 35%, var(--product-light) 0%, #d6d6d6 55%, var(--product-shade) 100%);
  }
</style>
</head>
<body>
  <div class="banner">
    <svg class="banner__beams" width="1200" height="465" viewBox="0 0 1200 465" aria-hidden="true">
      <defs>
        <linearGradient id="beam-fade-left" x1="1" y1="1" x2="0" y2="0">
          <stop offset="0" stop-color="var(--beam)"/>
          <stop offset="1" stop-color="rgba(255,255,255,0)"/>
        </linearGradient>
        <linearGradient id="beam-fade-right" x1="0" y1="1" x2="1" y2="0">
          <stop offset="0" stop-color="var(--beam)"/>
          <stop offset="1" stop-color="rgba(255,255,255,0)"/>
        </linearGradient>
      </defs>
      <polygon points="850,150 700,0 900,0 900,120" fill="url(#beam-fade-left)"/>
      <polygon points="990,160 1000,0 1200,0 1200,40" fill="url(#beam-fade-right)"/>
      <polygon points="930,160 880,0 960,0" fill="url(#beam-fade-left)" opacity="0.6"/>
    </svg>

    <h1 class="headline">
      <span class="headline__line">Outdoor Motion</span>
      <span class="headline__line">Detection Lighting</span>
    </h1>

    <a class="cta" href="#">
      Buy Now
      <svg class="cta__cursor" width="26" height="34" viewBox="0 0 26 34" aria-hidden="true">
        <path d="M2 2 L2 28 L9 21 L14 32 L19 30 L14 19 L24 19 Z" fill="#e07a10" stroke="#a85400" stroke-width="1.5" stroke-linejoin="round"/>
      </svg>
    </a>

    <div class="product-shot" role="img" aria-label="White wireless motion-sensor LED spotlight mounted on a swivel bracket, shining light upward"></div>
  </div>
</body>
</html>
```